Bierlogo gesucht
Zielgruppe
Bierherstellung / Zielgruppe sowohl Konsumenten von traditionellen Sorten als auch Liebhaber von Craftbeer
Aufgabenstellung
Aufgabe ist die Gestaltung eines Bieretiketts für den Brustbereich der Flasche / Weitere Auftragserweiterung Website und Cooperate Identity gewünscht / Lebensmittelrechtlich relevante Angaben sind zu berücksichtigen / Herstellung im Raum Oberbayern - Ammersee
Logo in Verbindung mit dem Namen "Haldbrunner" soll sowohl Qualität als auch Offenheit für neue Einflüsse, Rezepte, Inhaltsstoffe vermitteln, Stil kann gerne sehr einfach bzgl. Farbgebung aber einprägsam sein

```html
<!DOCTYPE html>
<html lang="de">
<head>
<meta charset="utf-8">
<title>Haldbrunner Bier – Etikett</title>
<link rel="stylesheet" href="https://fonts.googleapis.com/css2?family=Arimo:wght@700&family=Cinzel:wght@400;500&family=Open+Sans:wght@400;700&display=swap">
<style>
  :root {
    --label-black: #000000;
    --label-green: #1a6308;
    --label-green-dark: #0f3f05;
    --label-white: #ffffff;
    --paper: #ffffff;
    --art-light: #e6e6e6;
    --art-mid: #9a9a9a;
  }
  * { margin: 0; padding: 0; box-sizing: border-box; }
  html, body {
    width: 956px;
    height: 1200px;
    overflow: hidden;
    background: var(--paper);
  }
  .label {
    position: relative;
    width: 956px;
    height: 1200px;
    color: var(--label-white);
  }
  .label-shape {
    position: absolute;
    inset: 0;
  }
  .emblem-art {
    position: absolute;
    left: 330px;
    top: 70px;
    width: 306px;
    height: 298px;
    border-radius: 30px 30px 8px 8px;
    background: radial-gradient(ellipse at 50% 40%, var(--art-light) 0%, var(--art-mid) 100%);
    opacity: 0.85;
  }
  .tagline {
    position: absolute;
    left: 0;
    width: 956px;
    top: 382px;
    text-align: center;
    font-family: "Cinzel", serif;
    font-weight: 400;
    font-size: 50px;
    letter-spacing: 0.02em;
    line-height: 1;
  }
  .brand-name {
    position: absolute;
    left: 0;
    width: 956px;
    text-align: center;
    font-family: "Arimo", sans-serif;
    font-weight: 700;
    letter-spacing: -0.02em;
    line-height: 1;
  }
  .brand-name--primary { top: 517px; font-size: 122px; }
  .brand-name--secondary { top: 645px; font-size: 156px; }
  .ribbon-text {
    font-family: "Cinzel", serif;
    font-weight: 500;
    font-size: 46px;
    letter-spacing: 2px;
    fill: var(--label-white);
  }
  .legal-info {
    position: absolute;
    left: 0;
    width: 956px;
    top: 1014px;
    text-align: center;
    font-family: "Open Sans", sans-serif;
    font-size: 13px;
    line-height: 18.5px;
  }
  .legal-info .legal-heading { font-weight: 700; }
  .volume {
    position: absolute;
    left: 0;
    width: 956px;
    top: 1104px;
    text-align: center;
    font-family: "Open Sans", sans-serif;
    font-weight: 700;
    font-size: 16px;
  }
</style>
</head>
<body>
  <main class="label">
    <svg class="label-shape" width="956" height="1200" viewBox="0 0 956 1200" aria-hidden="false">
      <ellipse cx="478" cy="600" rx="427" ry="586" fill="var(--label-black)"/>
      <ellipse cx="478" cy="600" rx="413" ry="571" fill="none" stroke="var(--label-green)" stroke-width="6"/>

      <g class="ribbon">
        <polygon class="ribbon-tail" points="257,920 312,872 372,920 296,974" fill="var(--label-green)"/>
        <polygon class="ribbon-tail" points="699,920 644,872 584,920 660,974" fill="var(--label-green)"/>
        <polygon class="ribbon-fold" points="312,872 324,910 350,902" fill="var(--label-green-dark)"/>
        <polygon class="ribbon-fold" points="644,872 632,910 606,902" fill="var(--label-green-dark)"/>
        <path class="ribbon-band" d="M 282 858 Q 478 730 674 858 L 632 910 Q 478 800 324 910 Z" fill="var(--label-green)"/>
        <path id="ribbon-curve" d="M 300 890 Q 478 762 656 890" fill="none"/>
        <text class="ribbon-text">
          <textPath href="#ribbon-curve" startOffset="50%" text-anchor="middle">CRAFTBEER</textPath>
        </text>
      </g>
    </svg>

    <div class="emblem-art" role="img" aria-label="Illustration: Holzbottich mit Braupaddel, Gerstenähren, Maischgabel und Holzschlegel"></div>

    <p class="tagline">BIERSPEZIALITÄTEN</p>

    <h1 class="brand-name brand-name--primary">Haldbrunner</h1>
    <p class="brand-name brand-name--secondary">Bier</p>

    <div class="legal-info">
      <p class="legal-heading">ZUTATEN:</p>
      <p>Wasser, Gerstenmalz, Hopfen, Hefe</p>
      <p>D-86911 Seewang</p>
      <p>Alk. 4,9% vol.</p>
    </div>

    <p class="volume">℮ 50 cl</p>
  </main>
</body>
</html>
```